Billboard

we want our Hop & Skip logo really big, we need this to stand out

Use a really bold font for the wording as it's on a billboard on the highway

Hop & Skip Logo
perhaps on left hand side really large then have a slanting line and a different colour background for the other side.

Wording BELOW-bold

TOUR NOW

hopandskip.edu.au

Use one image,
I have attached other designs we have been using for our campaign so a similar look would be great.
specs- 1224 W × 324 H px JPEG

Target Market(s)
families

Industry/Entity Type
childcare

Target Market(s)

families

Industry/Entity Type

childcare

Requirements
Must have
• bold font and big logo

```html
<!DOCTYPE html>
<html lang="en">
<head>
<meta charset="UTF-8">
<title>Hop &amp; Skip Kindergarten – Tour Now Billboard</title>
<link href="https://fonts.googleapis.com/css2?family=Montserrat:wght@900&family=Nunito:wght@800&display=swap" rel="stylesheet">
<style>
  :root {
    --page-bg: #e9edf1;
    --billboard-blue: #29a8e0;
    --brand-yellow: #fff200;
    --brand-orange: #f9a533;
    --text-white: #ffffff;
    --photo-warm: #c9a27a;
    --photo-teal: #2d9bc7;
    --photo-green: #7a8a4a;
  }
  * { margin: 0; padding: 0; box-sizing: border-box; }
  html, body {
    width: 1200px;
    height: 900px;
    overflow: hidden;
    background: var(--page-bg);
  }
  .stage {
    width: 1200px;
    height: 900px;
    display: flex;
    align-items: center;
    justify-content: center;
  }
  .billboard {
    position: relative;
    width: 1120px;
    height: 296px;
    background: var(--billboard-blue);
    overflow: hidden;
  }
  .brand {
    position: absolute;
    left: 30px;
    top: 0;
    height: 100%;
    width: 270px;
    display: flex;
    align-items: center;
    gap: 12px;
  }
  .brand-dot {
    width: 40px;
    height: 40px;
    border-radius: 50%;
    background: var(--brand-yellow);
    flex: none;
  }
  .brand-name {
    font-family: 'Montserrat', sans-serif;
    font-weight: 900;
    font-size: 66px;
    line-height: 0.98;
    color: var(--text-white);
  }
  .brand-name span { display: block; white-space: nowrap; }
  .headline {
    position: absolute;
    left: 322px;
    top: 38px;
    font-family: 'Montserrat', sans-serif;
    font-weight: 900;
    font-size: 112px;
    line-height: 0.9;
    letter-spacing: -2px;
  }
  .headline span {
    display: block;
    width: fit-content;
    padding-right: 6px;
    background: linear-gradient(180deg, var(--brand-yellow) 0%, var(--brand-yellow) 38%, var(--brand-orange) 68%, var(--brand-yellow) 100%);
    -webkit-background-clip: text;
    background-clip: text;
    color: transparent;
  }
  .headline .line-one { margin-left: 36px; }
  .campaign-photo {
    position: absolute;
    right: 0;
    top: 0;
    width: 400px;
    height: 100%;
    background:
      radial-gradient(circle at 40% 45%, var(--photo-warm) 0%, transparent 45%),
      radial-gradient(circle at 85% 30%, var(--photo-green) 0%, transparent 40%),
      linear-gradient(135deg, var(--photo-teal) 0%, var(--photo-warm) 55%, var(--photo-teal) 100%);
    clip-path: polygon(12% 6%, 100% 0, 100% 100%, 8% 94%, 4% 78%, 0 70%, 6% 52%, 3% 36%, 9% 20%);
  }
  .web-address {
    position: absolute;
    right: 30px;
    bottom: 26px;
    font-family: 'Nunito', sans-serif;
    font-weight: 800;
    font-size: 34px;
    color: var(--text-white);
    background: var(--billboard-blue);
    padding: 2px 14px 4px;
    letter-spacing: 1px;
  }
</style>
</head>
<body>
  <main class="stage">
    <section class="billboard">
      <div class="brand">
        <span class="brand-dot"></span>
        <p class="brand-name"><span>Hop &amp;</span><span>Skip</span></p>
      </div>
      <h1 class="headline"><span class="line-one">TOUR</span><span class="line-two">NOW</span></h1>
      <div class="campaign-photo" role="img" aria-label="Photo of smiling kindergarten children in blue caps playing outdoors with an educator"></div>
      <p class="web-address">hopandskip.edu.au</p>
    </section>
  </main>
</body>
</html>
```